Flyer & Business Card for Lakeside Lens Guild photography courses

I need a flyer design for my company Lakeside Lens Guild - which offers photography classes for all levels in Geneva / Switzerland.

The flyer has to have an attractive visual at the front, and should highlight different types of classes and our teaching philosophy in the back.

Especially the images of Geneva (you can find some on lakesidelensguild.com and also on my photography website www.morvakimagery.com) will help to make people appreciate it's local.

Please check my website to learn more about my company, the logo, brand identity and the overall feeling:
https://www.lakesidelensguild.com

For the colors, I have used blue in the website and the logo, so it should be somehow compatible.

The final design should communicate fun courses offered by professional photographers that have received consistently 5 star ratings.

Target Market(s)

Geneva / Switzerland

Industry/Entity Type

Business

Contact Information for Business Card

Double sided - front could be a photo (or multiple photos that could be printed as part of one order from pex.com) and the back should communicate the brand identity.

Colors
0292cd
33a6d7
0555a3

```html
<!DOCTYPE html>
<html lang="en">
<head>
<meta charset="utf-8">
<title>Lakeside Lens Guild – Photography Courses Flyer</title>
<link rel="stylesheet" href="https://fonts.googleapis.com/css2?family=Pathway+Gothic+One&family=Varela+Round&display=swap">
<style>
  :root {
    --page-bg: #e4e4e4;
    --flyer-bg: #050608;
    --card-light: #29a6df;
    --card-dark: #0f6fbe;
    --title-blue: #33a6d7;
    --title-outline: #0555a3;
    --text-dark: #0b1a2a;
    --text-white: #ffffff;
    --badge-ring: #0292cd;
    --heart: #e0262e;
    --tick: #7cc23f;
  }
  * { box-sizing: border-box; margin: 0; padding: 0; }
  html, body { width: 1200px; height: 1000px; overflow: hidden; background: var(--page-bg); }
  .flyer {
    position: absolute; left: 261px; top: 20px;
    width: 678px; height: 960px;
    background: var(--flyer-bg);
    box-shadow: 0 4px 18px rgba(0,0,0,.25);
    overflow: hidden;
  }
  .visual { position: absolute; top: 0; height: 264px; }
  .visual--camera { left: 0; width: 234px; background: radial-gradient(ellipse at 55% 60%, #6b6f76 0%, #2a2d33 45%, #050608 75%); }
  .visual--portrait { left: 234px; width: 218px; background: linear-gradient(160deg, #c9c1a8 0%, #8c7a5a 45%, #3d3426 100%); }
  .visual--landscape { left: 456px; width: 222px; background: linear-gradient(180deg, #d9c89a 0%, #7d7a62 35%, #3c4a2c 65%, #5e6b38 100%); }
  .flyer-title {
    position: absolute; right: 10px; top: 209px;
    font-family: "Pathway Gothic One", sans-serif; font-size: 33px; font-weight: 400; line-height: 1.2;
    color: var(--title-blue); -webkit-text-stroke: 1px var(--title-outline);
    letter-spacing: 0; text-align: right; white-space: nowrap;
  }
  .course-grid {
    position: absolute; left: 12px; top: 266px;
    display: grid; grid-template-columns: repeat(3, 212px); grid-template-rows: repeat(3, 202px);
    column-gap: 11px; row-gap: 21px;
  }
  .card {
    position: relative; border-radius: 14px; padding: 10px 9px;
    background: var(--card-light); color: var(--text-dark);
    font-family: "Varela Round", sans-serif; font-size: 11.4px; line-height: 1.3;
  }
  .card p { padding-right: 2px; }
  .card--feature { background: var(--card-dark); color: var(--text-white); text-align: center; padding: 14px 12px; }
  .card-title {
    font-family: "Pathway Gothic One", sans-serif; font-weight: 400; font-size: 14.5px;
    text-transform: uppercase; color: var(--text-white); line-height: 1.4; margin-bottom: 12px;
  }
  .card--feature .card-title {
    font-family: "Varela Round", sans-serif; text-transform: none; font-size: 17px; margin-bottom: 12px;
  }
  .card strong { font-weight: 700; }
  .hours {
    position: absolute; right: -2px; bottom: -4px;
    width: 60px; height: 60px; border-radius: 50%;
    background: #fff; border: 3px solid var(--badge-ring);
    display: flex; align-items: center; justify-content: center;
    font-family: "Varela Round", sans-serif; font-size: 11px; color: #1b5f9a;
  }
  .icon { display: block; margin: 12px auto 0; }
  .site-url {
    position: absolute; left: 0; right: 0; top: 928px; text-align: center;
    font-family: "Varela Round", sans-serif; font-size: 15px; color: var(--text-white);
  }
</style>
</head>
<body>
<main class="flyer">
  <div class="visual visual--camera" role="img" aria-label="Photo of a vintage film camera hanging on a strap"></div>
  <div class="visual visual--portrait" role="img" aria-label="Artistic portrait photograph with textured headdress"></div>
  <div class="visual visual--landscape" role="img" aria-label="Landscape photo of a country road under a dramatic sky"></div>
  <h1 class="flyer-title">Digital Photography Courses for all levels</h1>

  <section class="course-grid">
    <article class="card">
      <h2 class="card-title">Intensive<br>Photography<br>Course for Beginners</h2>
      <p>You would like to make a serious step into photography over an intensive one day session during the weekend, and see the results immediately.</p>
      <span class="hours">7 hours</span>
    </article>
    <article class="card card--feature">
      <h2 class="card-title">Excellent Reviews</h2>
      <p>We deliver the best trainings in Geneva. How do we know? Check our excellent reviews from our previous students at our reviews page, on Facetalk and on Localia.</p>
      <svg class="icon" width="36" height="32" viewBox="0 0 36 32" aria-hidden="true"><path d="M18 31 C6 21 1 15 1 9 A8 8 0 0 1 18 6 A8 8 0 0 1 35 9 C35 15 30 21 18 31Z" fill="var(--heart)"/></svg>
    </article>
    <article class="card">
      <h2 class="card-title">Weekday Photography Classes for Beginners</h2>
      <p>You love photography and would love to focus on it during five weeks (classes &amp; homework) to make a serious improvement.</p>
      <span class="hours">10 hours</span>
    </article>

    <article class="card">
      <h2 class="card-title">One to One Private Photography Tuition</h2>
      <p>You have specific needs and want to learn directly from the professional with his/her undivided attention in the timings that suit you.</p>
      <span class="hours">6 hours</span>
    </article>
    <article class="card">
      <h2 class="card-title">Half-Day Photography Course for Beginners</h2>
      <p>You'd love to learn photography but have very limited time and feel confident to practice all the techniques yourself later.</p>
      <span class="hours">4 hours</span>
    </article>
    <article class="card card--feature">
      <h2 class="card-title">Result Focused</h2>
      <p>We promise to <strong>improve your photography immediately</strong>, showing you how to get different kind of results with practical examples. We won't lose time on theory.</p>
      <svg class="icon" width="40" height="30" viewBox="0 0 40 30" aria-hidden="true"><path d="M3 16 L14 27 L37 3" fill="none" stroke="var(--tick)" stroke-width="6" stroke-linecap="round" stroke-linejoin="round"/></svg>
    </article>

    <article class="card card--feature">
      <h2 class="card-title">Max 7 people</h2>
      <p>With classes no larger than 7 people, we guarantee a personal level of attention based on your experience level and equipment.</p>
      <svg class="icon" width="38" height="38" viewBox="0 0 38 38" aria-hidden="true"><circle cx="19" cy="11" r="9" fill="#5fb6e8"/><path d="M2 37 C2 26 9 22 19 22 C29 22 36 26 36 37Z" fill="#5fb6e8"/></svg>
    </article>
    <article class="card">
      <h2 class="card-title">Intermediate DSLR Photography Course</h2>
      <p>You already attended the intensive or half day class, or you already know the basic photography and want to improve.</p>
      <span class="hours">4 hours</span>
    </article>
    <article class="card">
      <h2 class="card-title">Street Photography Course<br>in Central Geneva</h2>
      <p>You know how to use your camera and would like to capture extraordinary moments from the ordinary life.</p>
      <span class="hours">4 hours</span>
    </article>
  </section>

  <p class="site-url">www.lakesidelensguild.com</p>
</main>
</body>
</html>
```